Looking for awesome business card design with attached existing logo

We are a water, mold, and fire damage restoration company called "Torvane Seco" Looking for an awesome business card that is edgy yet professional and unique. Show me what you got!

```html
<!DOCTYPE html>
<html lang="en">
<head>
<meta charset="utf-8">
<title>Torvane Seco – Business Card</title>
<link rel="stylesheet" href="https://fonts.googleapis.com/css2?family=Montserrat:wght@800&family=Open+Sans:wght@400;600&display=swap">
<style>
  :root {
    --canvas: #e9e7e4;
    --teal: #284955;
    --teal-text: #2b4b57;
    --gold: #c8901f;
    --red: #c0282f;
    --paper: #ffffff;
    --ink: #3a3a3a;
    --white: #ffffff;
  }
  * { margin: 0; padding: 0; box-sizing: border-box; }
  html, body {
    width: 1200px; height: 900px; overflow: hidden;
    background: var(--canvas);
  }
  .sheet {
    width: 1200px; height: 900px;
    display: flex; flex-direction: column; align-items: center; justify-content: center;
    gap: 40px;
  }
  .card {
    position: relative;
    width: 665px; height: 380px;
    border-radius: 32px;
    box-shadow: 0 10px 28px rgba(0,0,0,0.18);
    overflow: hidden;
  }
  .card--front {
    background: var(--teal);
    display: flex; align-items: center; justify-content: center;
  }
  .card--back { background: var(--paper); }

  .brand {
    display: flex; align-items: center; gap: 14px;
    font-family: 'Montserrat', sans-serif;
    font-weight: 800;
    letter-spacing: 2px;
    line-height: 1;
  }
  .brand__dot { border-radius: 50%; flex: none; }
  .brand--front { color: var(--white); font-size: 50px; }
  .brand--front .brand__dot { width: 26px; height: 26px; background: var(--white); }
  .brand--back {
    position: absolute; left: 44px; top: 120px;
    color: var(--teal-text); font-size: 34px;
  }
  .brand--back .brand__dot { width: 20px; height: 20px; background: var(--gold); }

  .person {
    position: absolute; right: 312px; top: 262px;
    text-align: right;
    font-family: 'Open Sans', sans-serif;
  }
  .person__name { color: var(--gold); font-weight: 600; font-size: 19px; letter-spacing: 0.3px; }
  .person__role { color: var(--ink); font-size: 17px; margin-top: 2px; }

  .divider {
    position: absolute; left: 368px; top: 222px;
    width: 1.5px; height: 118px; background: var(--red);
  }

  .contact {
    position: absolute; left: 384px; top: 226px;
    list-style: none;
    font-family: 'Open Sans', sans-serif;
    font-size: 15px; color: var(--ink);
  }
  .contact__item { display: flex; align-items: center; gap: 9px; height: 27px; }
  .contact__icon { width: 15px; height: 15px; flex: none; fill: var(--gold); }
</style>
</head>
<body>
<main class="sheet">
  <section class="card card--front" aria-label="Card front">
    <div class="brand brand--front">
      <span class="brand__dot"></span>
      <span class="brand__name">TORVANE SECO</span>
    </div>
  </section>

  <section class="card card--back" aria-label="Card back">
    <div class="brand brand--back">
      <span class="brand__dot"></span>
      <span class="brand__name">TORVANE SECO</span>
    </div>

    <div class="person">
      <p class="person__name">MARA KELLEN</p>
      <p class="person__role">Director</p>
    </div>

    <span class="divider"></span>

    <ul class="contact">
      <li class="contact__item">
        <svg class="contact__icon" viewBox="0 0 24 24"><path d="M6.6 10.8a15.1 15.1 0 0 0 6.6 6.6l2.2-2.2a1 1 0 0 1 1-.25 11.4 11.4 0 0 0 3.6.57 1 1 0 0 1 1 1V20a1 1 0 0 1-1 1A17 17 0 0 1 3 4a1 1 0 0 1 1-1h3.5a1 1 0 0 1 1 1c0 1.25.2 2.45.57 3.57a1 1 0 0 1-.25 1z"/></svg>
        <span>415-730-2861</span>
      </li>
      <li class="contact__item">
        <svg class="contact__icon" viewBox="0 0 24 24"><path d="M3 5h18a1 1 0 0 1 1 1v12a1 1 0 0 1-1 1H3a1 1 0 0 1-1-1V6a1 1 0 0 1 1-1zm1 2.2V17h16V7.2l-8 5.3z M4.6 7 12 11.9 19.4 7z"/></svg>
        <span>info@torvaneseco.com</span>
      </li>
      <li class="contact__item">
        <svg class="contact__icon" viewBox="0 0 24 24"><path d="M12 2a10 10 0 1 0 0 20 10 10 0 0 0 0-20zm0 2a8 8 0 0 1 7.7 6h-3.6a13 13 0 0 0-1.6-5.6A8 8 0 0 1 12 4zm-2.5.4A13 13 0 0 0 7.9 10H4.3a8 8 0 0 1 5.2-5.6zM4.3 14h3.6a13 13 0 0 0 1.6 5.6A8 8 0 0 1 4.3 14zm5.6 0h4.2a11 11 0 0 1-2.1 5.6A11 11 0 0 1 9.9 14zm0-4A11 11 0 0 1 12 4.4 11 11 0 0 1 14.1 10zm4.6 9.6a13 13 0 0 0 1.6-5.6h3.6a8 8 0 0 1-5.2 5.6z"/></svg>
        <span>www.torvaneseco.com</span>
      </li>
      <li class="contact__item">
        <svg class="contact__icon" viewBox="0 0 24 24"><path d="M12 2a7 7 0 0 0-7 7c0 5.2 7 13 7 13s7-7.8 7-13a7 7 0 0 0-7-7zm0 9.5A2.5 2.5 0 1 1 12 6.5a2.5 2.5 0 0 1 0 5z"/></svg>
        <span>12 Harbor Lane, Westfield 04</span>
      </li>
    </ul>
  </section>
</main>
</body>
</html>
```